oneness poster

a clean, elegant, simple text poster as follows (with some sort of glow or background consistent with the message:
MANIFESTO OF QUIET RIVERS

1. I am part of the world. The world is not outside of me, and I am not outside of the world. The world is in me, and I am in the world.

2. I am part of nature, and nature is part of me. I am what I am in my communication and communion with all living things. I am an irreducible and coherent whole with the web of life on the planet.

3. I am part of society, and society is part of me. I am what I am in my communication and communion with my fellow humans. I am an irreducible and coherent whole with the community of humans on the planet.

4. I am more than a skin-and-bone material organism: my body, and its cells and organs are manifestations of what is truly me: a self-sustaining, self-evolving dynamic system arising, persisting and evolving in interaction with everything around me.

5. I am one of the highest, most evolved manifestations of the drive toward coherence and wholeness in the universe. All systems drive toward coherence and wholeness in interaction with all other systems, and my essence is this cosmic drive. It is the same essence, the same spirit that is inherent in all the things that arise and evolve in nature, whether on this planet or elsewhere in the infinite reaches of space and time.

6. There are no absolute boundaries and divisions in this world, only transition points where one set of relations yields prevalence to another. In me, in this self-maintaining and self-evolving coherence- and wholeness-oriented system, the relations that integrate the cells and organs of my body are prevalent. Beyond my body other relations gain prevalence: those that drive toward coherence and wholeness in society and in nature.

7. The separate identity I attach to other humans and other things is but a convenient convention that facilitates my interaction with them. My family and my community are just as much “me” as the organs of my body. My body and mind, my family and my community, are interacting and interpenetrating, variously prevalent elements in the network of relations that encompasses all things in nature and the human world.

8. The whole gamut of concepts and ideas that separates my identity, or the identity of any person or community, from the identity of other persons and communities are manifestations of this convenient but arbitrary convention. There are only gradients distinguishing individuals from each other and from their environment and no real divisions and boundaries. There are no “others” in the world: we are all living systems and we are all part of each other.

9. Attempting to maintain the system I know as “me” through ruthless competition with the system I know as “you” is a grave mistake: it could damage the integrity of the embracing whole that frames both your life and mine. I cannot preserve my own life and wholeness by damaging that whole, even if damaging a part of it seems to bring me short-term advantage. When I harm you, or anyone else around me, I harm myself.

10. Collaboration, not competition, is the royal road to the wholeness that hallmarks healthy systems in the world. Collaboration calls for empathy and solidarity, and ultimately for love. I do not and cannot love myself if I do not love you and others around me: we are part of the same whole and so are part of each other.

11. The idea of “self-defense” even of “national defense,” needs to be rethought. Patriotism if it aims to eliminate adversaries by force, and heroism even in the well-meaning execution of that aim, are mistaken aspirations. A patriot and a hero who brandishes a sword or a gun is an enemy also to himself. Every weapon intended to hurt or kill is a danger to all. Comprehension, conciliation and forgiveness are not signs of weakness; they are signs of courage.

12. “The good” for me and for every person in the world is not the possession and accumulation of personal wealth. Wealth, in money or in any material resource, is but a means for maintaining myself in my environment. As exclusively mine, it commandeers part of the resources that all things need to share if they are to live and to thrive. Exclusive wealth is a threat to all people in the human community. And because I am a part of this community, in the final count it is a threat also to me, and to all who hold it.

13. Beyond the sacred whole we recognize as the world in its totality, only life and its development have what philosophers call intrinsic value; all other things have merely instrumental value: value insofar as they add to or enhance intrinsic value. Material things in the world, and the energies and substances they harbor or generate, have value only if and insofar they contribute to life and wellbeing in the web of life on this Earth.

14. Every healthy person has pleasure in giving: it is a higher pleasure than having. I am healthy and whole when I value giving over having. The true measure of my accomplishment and excellence is my readiness to give. Not the amount of what I give is the measure of my accomplishment and excellence, but the relation between what I give, and what my family and I need to live and to thrive.

15. A community that values giving over having is a community of healthy people, oriented toward thriving through empathy, solidarity, and love among its members. Sharing enhances the community of life, while possessing and accumulating creates demarcation, invites competition, and fuels envy. The share-society is the norm for all the communities of life on the planet; the have-society is typical only of modern-day humanity, and it is an aberration.
.

16. I acknowledge my role and responsibility in evolving a planetary consciousness in me, and by example in others around me. I have been part of the aberration of human consciousness in the modern age, and now wish to become part of the evolution that overcomes the aberration and heals the wounds inflicted by it. This is my right as well as my duty, as a conscious member of a conscious species on a precious and now critically endangered planet.

• MANIFESTO OF QUIET RIVERS

.

• a very very simple glow in the background or other look consistent with the all-is-one (OM) message. A strong, almost spirtual feel.
• no flowery designs, no distractions. Nothing cute.

```html
<!DOCTYPE html>
<html lang="en">
<head>
<meta charset="utf-8">
<title>Manifesto of Quiet Rivers</title>
<link href="https://fonts.googleapis.com/css2?family=Nunito:wght@600;800&display=swap" rel="stylesheet">
<style>
  :root{
    --paper:#ffffff;
    --ink-title:#1b5f9e;
    --ink-disc:#ffffff;
    --c1:#3bbfd0; --c2:#2ea8dc; --c3:#1f9ad6; --c4:#46b3e6;
    --c5:#2b8fd1; --c6:#1d7fc4; --c7:#53c0e8; --c8:#2f9fd8;
    --c9:#3aa8d9; --c10:#4ec1d6; --c11:#2a8ccc; --c12:#5cc6e6;
    --c13:#2394d4; --c14:#3fb7dc; --c15:#1e86c8; --c16:#48b0e2;
  }
  *{margin:0;padding:0;box-sizing:border-box}
  html,body{width:849px;height:1200px;overflow:hidden;background:var(--paper)}
  .poster{position:relative;width:849px;height:1200px;overflow:hidden;background:var(--paper);font-family:"Nunito",sans-serif}
  .disc{
    position:absolute;
    left:calc(var(--x) * 1px - var(--r) * 1px);
    top:calc(var(--y) * 1px - var(--r) * 1px);
    width:calc(var(--r) * 2px);
    height:calc(var(--r) * 2px);
    border-radius:50%;
    background:var(--fill);
    display:flex;align-items:center;justify-content:center;
    overflow:hidden;
  }
  .statement{
    width:76%;
    color:var(--ink-disc);
    font-weight:600;
    font-size:var(--fs,8.5px);
    line-height:1.24;
    text-align:center;
  }
  .statement b{font-weight:800}
  .title-disc{background:var(--paper)}
  .title{
    color:var(--ink-title);
    font-weight:800;
    font-size:31px;
    line-height:1.02;
    text-align:center;
    text-transform:lowercase;
    letter-spacing:-0.5px;
  }
</style>
</head>
<body>
<main class="poster">

  <div class="disc" style="--x:100;--y:110;--r:100;--fill:var(--c1);--fs:10.5px">
    <p class="statement"><b>1.</b> I am part of the world. The world is not outside of me, and I am not outside of the world. The world is in me, and I am in the world.</p>
  </div>

  <div class="disc" style="--x:280;--y:255;--r:90;--fill:var(--c2);--fs:9px">
    <p class="statement"><b>2.</b> I am part of nature, and nature is part of me. I am what I am in my communication and communion with all living things. I am an irreducible and coherent whole with the web of life on the planet.</p>
  </div>

  <div class="disc" style="--x:390;--y:95;--r:85;--fill:var(--c3);--fs:8.5px">
    <p class="statement"><b>3.</b> I am part of society, and society is part of me. I am what I am in my communication and communion with my fellow humans. I am an irreducible and coherent whole with the community of humans on the planet.</p>
  </div>

  <div class="disc" style="--x:545;--y:215;--r:105;--fill:var(--c4);--fs:8.6px">
    <p class="statement"><b>4.</b> I am more than a skin-and-bone material organism: my body, and its cells and organs are manifestations of what is truly me: a self-sustaining, self-evolving dynamic system arising, persisting and evolving in interaction with everything around me.</p>
  </div>

  <div class="disc" style="--x:745;--y:115;--r:120;--fill:var(--c5);--fs:8.4px">
    <p class="statement"><b>5.</b> I am one of the highest, most evolved manifestations of the drive toward coherence and wholeness in the universe. All systems drive toward coherence and wholeness in interaction with all other systems, and my essence is this cosmic drive. It is the same essence, the same spirit that is inherent in all the things that arise and evolve in nature, whether on this planet or elsewhere in the infinite reaches of space and time.</p>
  </div>

  <div class="disc" style="--x:750;--y:375;--r:120;--fill:var(--c6);--fs:8.4px">
    <p class="statement"><b>6.</b> There are no absolute boundaries and divisions in this world, only transition points where one set of relations yields prevalence to another. In me, in this self-maintaining and self-evolving coherence- and wholeness-oriented system, the relations that integrate the cells and organs of my body are prevalent. Beyond my body other relations gain prevalence: those that drive toward coherence and wholeness in society and in nature.</p>
  </div>

  <div class="disc" style="--x:520;--y:455;--r:120;--fill:var(--c7);--fs:8.4px">
    <p class="statement"><b>7.</b> The separate identity I attach to other humans and other things is but a convenient convention that facilitates my interaction with them. My family and my community are just as much “me” as the organs of my body. My body and mind, my family and my community, are interacting and interpenetrating, variously prevalent elements in the network of relations that encompasses all things in nature and the human world.</p>
  </div>

  <div class="disc" style="--x:290;--y:520;--r:115;--fill:var(--c8);--fs:8.2px">
    <p class="statement"><b>8.</b> The whole gamut of concepts and ideas that separates my identity, or the identity of any person or community, from the identity of other persons and communities are manifestations of this convenient but arbitrary convention. There are only gradients distinguishing individuals from each other and from their environment and no real divisions and boundaries. There are no “others” in the world: we are all living systems and we are all part of each other.</p>
  </div>

  <div class="disc" style="--x:100;--y:395;--r:112;--fill:var(--c9);--fs:8.3px">
    <p class="statement"><b>9.</b> Attempting to maintain the system I know as “me” through ruthless competition with the system I know as “you” is a grave mistake: it could damage the integrity of the embracing whole that frames both your life and mine. I cannot preserve my own life and wholeness by damaging that whole, even if damaging a part of it seems to bring me short-term advantage. When I harm you, or anyone else around me, I harm myself.</p>
  </div>

  <div class="disc" style="--x:100;--y:650;--r:108;--fill:var(--c10);--fs:8.4px">
    <p class="statement"><b>10.</b> Collaboration, not competition, is the royal road to the wholeness that hallmarks healthy systems in the world. Collaboration calls for empathy and solidarity, and ultimately for love. I do not and cannot love myself if I do not love you and others around me: we are part of the same whole and so are part of each other.</p>
  </div>

  <div class="disc" style="--x:290;--y:790;--r:118;--fill:var(--c11);--fs:8.2px">
    <p class="statement"><b>11.</b> The idea of “self-defense” even of “national defense,” needs to be rethought. Patriotism if it aims to eliminate adversaries by force, and heroism even in the well-meaning execution of that aim, are mistaken aspirations. A patriot and a hero who brandishes a sword or a gun is an enemy also to himself. Every weapon intended to hurt or kill is a danger to all. Comprehension, conciliation and forgiveness are not signs of weakness; they are signs of courage.</p>
  </div>

  <div class="disc" style="--x:525;--y:735;--r:120;--fill:var(--c12);--fs:8.2px">
    <p class="statement"><b>12.</b> “The good” for me and for every person in the world is not the possession and accumulation of personal wealth. Wealth, in money or in any material resource, is but a means for maintaining myself in my environment. As exclusively mine, it commandeers part of the resources that all things need to share if they are to live and to thrive. Exclusive wealth is a threat to all people in the human community. And because I am a part of this community, in the final count it is a threat also to me, and to all who hold it.</p>
  </div>

  <div class="disc" style="--x:745;--y:640;--r:118;--fill:var(--c13);--fs:8.3px">
    <p class="statement"><b>13.</b> Beyond the sacred whole we recognize as the world in its totality, only life and its development have what philosophers call intrinsic value; all other things have merely instrumental value: value insofar as they add to or enhance intrinsic value. Material things in the world, and the energies and substances they harbor or generate, have value only if and insofar they contribute to life and wellbeing in the web of life on this Earth.</p>
  </div>

  <div class="disc" style="--x:750;--y:900;--r:110;--fill:var(--c14);--fs:8.3px">
    <p class="statement"><b>14.</b> Every healthy person has pleasure in giving: it is a higher pleasure than having. I am healthy and whole when I value giving over having. The true measure of my accomplishment and excellence is my readiness to give. Not the amount of what I give is the measure of my accomplishment and excellence, but the relation between what I give, and what my family and I need to live and to thrive.</p>
  </div>

  <div class="disc" style="--x:530;--y:985;--r:120;--fill:var(--c15);--fs:8.3px">
    <p class="statement"><b>15.</b> A community that values giving over having is a community of healthy people, oriented toward thriving through empathy, solidarity, and love among its members. Sharing enhances the community of life, while possessing and accumulating creates demarcation, invites competition, and fuels envy. The share-society is the norm for all the communities of life on the planet; the have-society is typical only of modern-day humanity, and it is an aberration.</p>
  </div>

  <div class="disc" style="--x:300;--y:1060;--r:120;--fill:var(--c16);--fs:8.4px">
    <p class="statement"><b>16.</b> I acknowledge my role and responsibility in evolving a planetary consciousness in me, and by example in others around me. I have been part of the aberration of human consciousness in the modern age, and now wish to become part of the evolution that overcomes the aberration and heals the wounds inflicted by it. This is my right as well as my duty, as a conscious member of a conscious species on a precious and now critically endangered planet.</p>
  </div>

  <div class="disc title-disc" style="--x:95;--y:990;--r:95">
    <h1 class="title">manifesto<br>of quiet<br>rivers</h1>
  </div>

</main>
</body>
</html>
```